Website design for dressage horse training business

Looking to develop a new website design for a dressage horse training website. We want to change from a single landing page to one with multiple pages.
You are free to use your creativity to design the main landing page. This is the only page you need to design at this point. I would encourage looking at other Dressage Training websites to get a feel for what is typically on them. A few websites are listed below although I think the design of them could be better.
Notes:
- Menu to include: Home, Services, News Room, Blog, About Us, Contact,
- FAQ section on main page
- Logo to remain the same - the logo attached is not the correct color so change to match existing color.
- Change 'Sponsors' to 'Partnerships' on main page
Here is the link to the current site:
https://larkvalebarn.com/
Example sites
https://www.quillbrookstablesna.com/
https://corinnahaldwickdressage.com/
Older women with disposable income

```html
<!DOCTYPE html>
<html lang="en">
<head>
<meta charset="utf-8">
<title>Larkvale Barn – Dressage &amp; Sport Horse Training</title>
<link href="https://fonts.googleapis.com/css2?family=Lato:ital,wght@0,400;0,700;0,900;1,400&display=swap" rel="stylesheet">
<style>
:root{
  --red:#b3170f;
  --red-bright:#c8231a;
  --ink:#222;
  --text:#444;
  --muted:#777;
  --line:#e3e3e3;
  --blush:#fbf5f5;
  --white:#fff;
}
*{box-sizing:border-box;margin:0;padding:0}
html,body{width:1200px;height:3678px;overflow:hidden}
body{font-family:"Lato",sans-serif;color:var(--text);background:var(--white);position:relative}
.abs{position:absolute}
a{color:inherit;text-decoration:none}

/* header */
.call-icon{left:141px;top:64px}
.call-label{left:197px;top:64px;font-size:14px;font-weight:700;color:var(--ink)}
.call-number{left:197px;top:82px;font-size:22px;font-weight:700;color:var(--ink)}
.brand{left:0;width:1200px;top:46px;text-align:center;font-size:50px;font-weight:400;color:var(--red);letter-spacing:1px}
.social{top:65px;width:42px;height:42px;border:2px solid var(--ink);border-radius:50%}
.nav{top:161px;left:0;width:1200px;height:61px;border-top:1px solid var(--line);border-bottom:1px solid var(--line)}
.nav ul{list-style:none;display:flex;justify-content:center;gap:28px;padding-top:22px;font-size:14px;color:var(--ink)}
.nav li.active{color:var(--red);position:relative}
.nav li.active::before{content:"";position:absolute;left:-14px;right:-14px;top:-31px;height:5px;background:var(--red);border-radius:3px}

/* hero */
.hero{left:0;top:222px;width:1200px;height:625px;background:linear-gradient(120deg,#3a4a3e 0%,#6a4a30 35%,#2f3a34 60%,#8a5a36 100%)}
.hero h1{left:141px;top:186px;font-size:50px;line-height:56px;font-weight:900;color:var(--white);text-transform:uppercase}
.btn{display:flex;align-items:center;justify-content:center;border-radius:24px;font-weight:700;text-transform:uppercase}
.btn-red{background:var(--red);color:var(--white)}
.hero .btn{left:143px;top:378px;width:172px;height:45px;font-size:15px}
.dot{width:14px;height:14px;border:2px solid var(--white);border-radius:50%;left:1110px}

/* about */
.about-photo{left:0;top:847px;width:618px;height:524px;background:linear-gradient(180deg,#b9cbe0 0%,#8aa56a 35%,#c9b59a 60%,#6d8a4a 100%)}
.about{left:618px;top:847px;width:582px;height:524px;background:var(--blush)}
.about .eyebrow{left:85px;top:68px;font-size:32px;font-weight:700;color:var(--red)}
.about h2{left:85px;top:112px;font-size:44px;font-weight:700;color:var(--ink)}
.about p{left:85px;top:186px;width:360px;font-size:13.5px;line-height:24px;color:var(--text)}
.about .btn{left:85px;top:406px;width:168px;height:45px;font-size:15px}

/* faq */
.faq-title{left:145px;top:1468px;font-size:36px;font-weight:900;color:var(--ink)}
.faq-list{left:143px;top:1530px;list-style:none;font-size:12.5px;color:var(--ink)}
.faq-list li{display:flex;align-items:center;gap:16px;height:30px}
.faq-text{left:145px;top:1652px;width:470px;font-size:13.5px;line-height:26px;color:var(--text)}
.btn-outline{border:2px solid var(--red);color:var(--red)}
.faq-btn{left:143px;top:1727px;width:140px;height:39px;font-size:15px;font-weight:400}
.faq-photo{left:641px;top:1381px;width:559px;height:480px;border-left:4px solid var(--red);border-bottom:4px solid var(--red);background:linear-gradient(160deg,#8a7a62 0%,#5d7a4a 40%,#c8c2b2 70%,#7a5a3a 100%)}

/* blogs */
.blogs-title{left:0;width:1200px;top:1935px;text-align:center;font-size:37px;font-weight:700;color:var(--ink)}
.card{top:2016px;width:287px;height:445px;border:1px solid var(--line);border-radius:4px;background:var(--white)}
.card.raised{box-shadow:0 4px 14px rgba(0,0,0,.08)}
.card .thumb{left:3px;top:3px;width:280px;height:225px}
.card .date{left:22px;top:254px;font-size:15px;color:var(--red);display:flex;gap:8px;align-items:center}
.card p{left:22px;top:287px;width:230px;font-size:14px;line-height:20px;color:var(--text)}
.card .btn{left:22px;top:380px;width:125px;height:34px;border:2px solid var(--ink);font-size:11px;color:var(--ink);border-radius:20px}

/* contact */
.contact{left:0;top:2546px;width:1200px;height:695px;background:linear-gradient(135deg,#2a2e22 0%,#3a4a2e 40%,#2b2a26 70%,#1e1f1c 100%)}
.contact h2{left:0;width:1200px;top:95px;text-align:center;font-size:39px;font-weight:700;color:var(--white)}
.contact .rule{left:570px;top:152px;width:60px;height:3px;background:var(--red)}
.contact .lead{left:0;width:1200px;top:176px;text-align:center;font-size:14px;font-style:italic;color:var(--white)}
.field{background:var(--white);font-size:14px;color:#555;padding:0 23px;display:flex;align-items:center}
.field.tall{align-items:flex-start;padding-top:16px}
.contact .btn{left:507px;top:502px;width:186px;height:45px;font-size:16px}

/* footer */
.footer-brand{left:145px;top:3318px;font-size:34px;font-weight:400;color:var(--red)}
.badge-oval{left:150px;top:3408px;width:125px;height:46px;border-radius:50%;background:#8b2a1c}
.badge-square{left:155px;top:3462px;width:105px;height:98px;background:#e5e5e5}
.foot-h{font-size:19px;font-weight:700;color:var(--ink);text-transform:uppercase}
.foot-p{font-size:13.5px;line-height:22px;color:var(--text)}
.foot-input{left:384px;width:272px;height:38px;border:1px solid #ccc;border-radius:20px;font-size:12px;padding-left:14px;display:flex;align-items:center;color:#555}
.sub-btn{left:384px;top:3540px;width:138px;height:34px;font-size:14px;border-radius:18px}
.ci{left:703px;display:flex;gap:18px;font-size:13.5px;line-height:20px;color:var(--ink)}
.links{left:940px;top:3380px;list-style:none;font-size:13.5px;line-height:27px;color:var(--text)}
.divider{left:143px;top:3622px;width:914px;height:1px;background:var(--line)}
.copy{left:0;width:1200px;top:3643px;text-align:center;font-size:12px;color:var(--ink)}
</style>
</head>
<body>

<!-- header -->
<svg class="abs call-icon" width="40" height="40" viewBox="0 0 24 24" fill="none" stroke="#b3170f" stroke-width="1.6"><path d="M5 3h4l2 5-2.5 1.5a11 11 0 0 0 6 6L16 13l5 2v4a2 2 0 0 1-2 2A17 17 0 0 1 3 5a2 2 0 0 1 2-2z"/><path d="M15 3a6 6 0 0 1 6 6M15 7a2 2 0 0 1 2 2"/></svg>
<div class="abs call-label">CALL US</div>
<div class="abs call-number">515-555-0172</div>
<div class="abs brand">Larkvale Barn</div>
<div class="abs social" style="left:859px" role="img" aria-label="Social profile link"></div>
<div class="abs social" style="left:913px" role="img" aria-label="Social profile link"></div>
<div class="abs social" style="left:967px" role="img" aria-label="Social profile link"></div>
<div class="abs social" style="left:1013px" role="img" aria-label="Video channel link"></div>

<nav class="abs nav">
  <ul>
    <li class="active">HOME</li>
    <li>TRAINING AND LESSONS</li>
    <li>ABOUT US</li>
    <li>PARTNERSHIPS</li>
    <li>FOR SALE</li>
    <li>CALENDAR</li>
    <li>PHOTO GALLERY</li>
    <li>CONTACT</li>
  </ul>
</nav>

<!-- hero -->
<section class="abs hero" role="img" aria-label="Close-up photograph of a dressage saddle on a bay horse">
  <h1 class="abs">Central Iowa's<br>Premier Dressage &amp;<br>Sport Horse Training</h1>
  <a class="abs btn btn-red">Learn More</a>
  <div class="abs dot" style="top:305px;border-color:var(--red)"></div>
  <div class="abs dot" style="top:332px"></div>
  <div class="abs dot" style="top:357px"></div>
  <svg class="abs" style="left:0;top:588px" width="1200" height="37" viewBox="0 0 1200 37" preserveAspectRatio="none">
    <polygon points="0,20 0,37 600,37 0,10" fill="#b3170f"/>
    <polygon points="1200,10 1200,37 600,37" fill="#b3170f"/>
    <polygon points="0,37 600,37 0,28 " fill="#fff"/>
    <polygon points="1200,37 600,37 1200,28" fill="#fff"/>
  </svg>
</section>

<!-- about -->
<div class="abs about-photo" role="img" aria-label="Photograph of the trainer standing between two horses at an outdoor arena"></div>
<section class="abs about">
  <div class="abs eyebrow">About Us</div>
  <h2 class="abs">Larkvale Barn</h2>
  <p class="abs">FEI rider and trainer, Helena Rourke began her riding career at a young age. She went up through the ranks of Pony Club and with an emphasis and focus in eventing. During college, Helena worked for a small breeder starting young horses. Helena loves starting young horses including starting and guiding them in a correct and quiet way to help them flourish. Her training focuses on gymnastic training incorporating ground</p>
  <a class="abs btn btn-red">Learn More</a>
</section>

<!-- faq -->
<h2 class="abs faq-title">FAQ</h2>
<ul class="abs faq-list">
  <li><svg width="15" height="15" viewBox="0 0 16 16" fill="none" stroke="#b3170f" stroke-width="1.5"><circle cx="8" cy="8" r="7"/><path d="M4 8h7M8 5l3 3-3 3"/></svg>para citar tu evaluación y diagnostico</li>
  <li><svg width="15" height="15" viewBox="0 0 16 16" fill="none" stroke="#b3170f" stroke-width="1.5"><circle cx="8" cy="8" r="7"/><path d="M4 8h7M8 5l3 3-3 3"/></svg>Revisar los resultados y recomendaciónes de reporte diagnóstico</li>
  <li><svg width="15" height="15" viewBox="0 0 16 16" fill="none" stroke="#b3170f" stroke-width="1.5"><circle cx="8" cy="8" r="7"/><path d="M4 8h7M8 5l3 3-3 3"/></svg>Fijar días y horario de tu curso</li>
  <li><svg width="15" height="15" viewBox="0 0 16 16" fill="none" stroke="#b3170f" stroke-width="1.5"><circle cx="8" cy="8" r="7"/><path d="M4 8h7M8 5l3 3-3 3"/></svg>Ahora esta listo para iniciar tu curso personalizado con EES</li>
</ul>
<p class="abs faq-text">Sed ut perspiciatis unde omnis iste natus error sit voluptatem accustium doloremque laudantium, totam rem aperiam,</p>
<a class="abs btn btn-outline faq-btn">Read More</a>
<div class="abs faq-photo" role="img" aria-label="Photograph of a rider in dressage attire on a pinto horse beside a wooden barn"></div>

<!-- blogs -->
<h2 class="abs blogs-title">Latest Blogs</h2>

<article class="abs card" style="left:143px">
  <div class="abs thumb" role="img" aria-label="Photograph of a rider on a pinto horse in a dressage arena" style="background:linear-gradient(160deg,#3f6a3a,#8a9a7a 60%,#d8c9a0)"></div>
  <div class="abs date"><svg width="12" height="12" viewBox="0 0 12 12" fill="#444"><rect x="1" y="2" width="10" height="9"/><rect x="2" y="4" width="8" height="6" fill="#fff"/></svg>16TH MARCH 2021</div>
  <p class="abs">Larkvale Barn offers both full and half time training options with Helena Rourke. There is much flexibility with both</p>
  <a class="abs btn">Learn More</a>
</article>

<article class="abs card raised" style="left:456px">
  <div class="abs thumb" role="img" aria-label="Photograph of the trainer with a ribboned pinto horse" style="background:linear-gradient(160deg,#5a4a3a,#9a8a72 55%,#c7c2b8)"></div>
  <div class="abs date"><svg width="12" height="12" viewBox="0 0 12 12" fill="#444"><rect x="1" y="2" width="10" height="9"/><rect x="2" y="4" width="8" height="6" fill="#fff"/></svg>15TH MARCH 2021</div>
  <p class="abs">Larkvale Barn offers both full and half time training options with Helena Rourke. There is much flexibility with both</p>
  <a class="abs btn">Learn More</a>
</article>

<article class="abs card" style="left:771px">
  <div class="abs thumb" role="img" aria-label="Photograph of a horse and rider at a championship ceremony" style="background:linear-gradient(170deg,#23348a,#3a2a5a 50%,#6a3a2a 80%,#3a5a2a)"></div>
  <div class="abs date"><svg width="12" height="12" viewBox="0 0 12 12" fill="#444"><rect x="1" y="2" width="10" height="9"/><rect x="2" y="4" width="8" height="6" fill="#fff"/></svg>14TH MARCH 2021</div>
  <p class="abs">Larkvale Barn offers both full and half time training options with Helena Rourke. There is much flexibility with both</p>
  <a class="abs btn">Learn More</a>
</article>

<!-- contact -->
<section class="abs contact" role="img" aria-label="Dark photograph of a saddled horse as background for the contact form">
  <svg class="abs" style="left:0;top:0" width="1200" height="50" viewBox="0 0 1200 50" preserveAspectRatio="none">
    <polygon points="0,0 1200,0 1200,50 600,0 0,50" fill="#fff"/>
    <polygon points="0,50 600,0 600,8 0,38" fill="#b3170f"/>
    <polygon points="1200,50 600,0 600,8 1200,38" fill="#b3170f"/>
  </svg>
  <h2 class="abs">Get In Touch</h2>
  <div class="abs rule"></div>
  <p class="abs lead">If you are interested in learning more about Larkvale Barn's services or availability for training or lessons, please contact us below!</p>
  <div class="abs field" style="left:199px;top:247px;width:370px;height:62px">Your name</div>
  <div class="abs field" style="left:199px;top:327px;width:370px;height:62px">Email address</div>
  <div class="abs field" style="left:199px;top:407px;width:370px;height:62px">Phone</div>
  <div class="abs field" style="left:599px;top:247px;width:402px;height:62px">Subject</div>
  <div class="abs field tall" style="left:599px;top:327px;width:402px;height:142px">Message</div>
  <a class="abs btn btn-red">Submit</a>
  <svg class="abs" style="left:0;top:645px" width="1200" height="50" viewBox="0 0 1200 50" preserveAspectRatio="none">
    <polygon points="0,0 0,22 600,50 0,12" fill="#b3170f"/>
    <polygon points="1200,0 1200,22 600,50 1200,12" fill="#b3170f"/>
    <polygon points="0,22 600,50 0,50" fill="#fff"/>
    <polygon points="1200,22 600,50 1200,50" fill="#fff"/>
  </svg>
</section>

<!-- footer -->
<div class="abs footer-brand">Larkvale Barn</div>
<div class="abs badge-oval" role="img" aria-label="Partner badge"></div>
<div class="abs badge-square" role="img" aria-label="Partner badge"></div>

<div class="abs foot-h" style="left:384px;top:3330px">Sign Up For Newsletter</div>
<p class="abs foot-p" style="left:384px;top:3377px;width:285px">excepteur sint occaecat cupidatat non proident, sunt in culpa qui officia deserunt</p>
<div class="abs foot-input" style="top:3455px">Enter Name</div>
<div class="abs foot-input" style="top:3505px">Enter email</div>
<a class="abs btn btn-red sub-btn">Subscribe</a>

<div class="abs foot-h" style="left:703px;top:3332px">Contact Us</div>
<div class="abs ci" style="top:3382px"><svg width="18" height="20" viewBox="0 0 24 24" fill="#b3170f"><path d="M12 2a7 7 0 0 0-7 7c0 5 7 13 7 13s7-8 7-13a7 7 0 0 0-7-7zm0 9.5A2.5 2.5 0 1 1 12 6.5a2.5 2.5 0 0 1 0 5z"/></svg><span>Des Moines<br>Iowa, USA</span></div>
<div class="abs ci" style="top:3443px"><svg width="18" height="18" viewBox="0 0 24 24" fill="#b3170f"><path d="M6 2h4l2 5-3 2a12 12 0 0 0 6 6l2-3 5 2v4a2 2 0 0 1-2 2A18 18 0 0 1 4 4a2 2 0 0 1 2-2z"/></svg><span>Phone:<br>515-555-0172</span></div>
<div class="abs ci" style="top:3508px"><svg width="18" height="16" viewBox="0 0 24 20" fill="#b3170f"><rect x="1" y="2" width="22" height="16" rx="1"/><path d="M2 3l10 8 10-8" stroke="#fff" stroke-width="2" fill="none"/></svg><span>Email:<br>info@larkvalebarn.com</span></div>

<div class="abs foot-h" style="left:936px;top:3332px">Quick Links</div>
<ul class="abs links">
  <li>Home</li><li>Services</li><li>News Room</li><li>Blog</li><li>About Us</li><li>Contact</li>
</ul>

<div class="abs divider"></div>
<div class="abs copy">Larkvale Barn © 2021 All Rights Reserved | Privacy Policy</div>

</body>
</html>
```